Billboard design for property management

DEADLINE 3RD APRIL 2022
I need a billboard design sized 390cm x 275 cm with 10cm bleed.

It needs to attract potential homeowners who want to make money by renting out their property to holidays

White background with orange and grey (as in the logo) maybe with an image. It must somehow, incorporate the boost your bookings attached.

Needs to show web address and phone number

```html
<!DOCTYPE html>
<html lang="en">
<head>
<meta charset="utf-8">
<title>Boost Your Bookings – Billboard</title>
<link href="https://fonts.googleapis.com/css2?family=Anton&family=Montserrat:wght@700;800&display=swap" rel="stylesheet">
<style>
  :root {
    --orange: #e46f24;
    --orange-deep: #d9621c;
    --grey-dark: #3a3a3a;
    --white: #ffffff;
    --paper: #f4f4f4;
    --stage: #dfe3e8;
    --money-light: #e9ebe6;
    --money-mid: #b9beb6;
    --money-dark: #7d847c;
  }
  * { margin: 0; padding: 0; box-sizing: border-box; }
  html, body { width: 1200px; height: 900px; overflow: hidden; background: var(--stage); }
  .billboard {
    position: absolute; left: 50px; top: 62px;
    width: 1100px; height: 776px;
    background: linear-gradient(160deg, var(--white) 0%, var(--paper) 100%);
    overflow: hidden;
    box-shadow: 0 10px 30px rgba(0,0,0,.15);
  }
  .billboard__shapes { position: absolute; inset: 0; }
  .brand-mark {
    position: absolute; left: 150px; top: 62px;
    display: flex; align-items: center; gap: 12px;
    font-family: 'Montserrat', sans-serif; font-weight: 800;
    color: var(--orange); font-size: 26px; letter-spacing: .5px;
  }
  .brand-mark__dot { width: 26px; height: 26px; border-radius: 50%; background: var(--orange); }
  .brand-mark__name { line-height: 1; }
  .headline {
    position: absolute; left: 80px; top: 150px;
    font-family: 'Anton', sans-serif; line-height: .95;
  }
  .headline__boost { font-size: 190px; color: var(--orange); letter-spacing: 4px; }
  .headline__sub { font-size: 58px; color: var(--grey-dark); letter-spacing: 2px; margin-top: 4px; }
  .offer {
    position: absolute; left: 70px; top: 440px; width: 470px;
    color: var(--white); font-family: 'Montserrat', sans-serif;
  }
  .offer__with {
    display: flex; align-items: center; gap: 14px;
    font-family: 'Anton', sans-serif; font-size: 38px; letter-spacing: 2px;
  }
  .offer__with::before, .offer__with::after {
    content: ""; flex: 1; height: 4px; background: var(--white);
  }
  .offer__with::before { flex: 2.2; }
  .offer__brand { display: flex; align-items: center; gap: 14px; margin-top: 14px; }
  .offer__brand-dot { width: 60px; height: 60px; border-radius: 50%; background: var(--white); flex: none; }
  .offer__brand-text { display: flex; flex-direction: column; font-weight: 800; }
  .offer__brand-name { font-size: 44px; line-height: 1; letter-spacing: .5px; }
  .offer__brand-sub { font-size: 19px; line-height: 1.2; margin-top: 4px; letter-spacing: .5px; }
  .offer__phone { font-weight: 800; font-size: 48px; margin-top: 12px; letter-spacing: 1px; white-space: nowrap; }
  .web-bar {
    position: absolute; left: 80px; top: 690px; width: 540px; height: 56px;
    background: var(--white); display: flex; align-items: center; gap: 16px; padding-left: 40px;
    font-family: 'Montserrat', sans-serif; font-weight: 700; font-size: 24px;
    color: var(--orange); letter-spacing: 4px; white-space: nowrap;
  }
  .web-bar__icon { width: 28px; height: 28px; flex: none; }
</style>
</head>
<body>
  <main class="billboard">
    <svg class="billboard__shapes" width="1100" height="776" viewBox="0 0 1100 776">
      <defs>
        <linearGradient id="moneyTone" x1="0" y1="0" x2="1" y2="1">
          <stop offset="0" stop-color="var(--money-light)"/>
          <stop offset=".55" stop-color="var(--money-mid)"/>
          <stop offset="1" stop-color="var(--money-dark)"/>
        </linearGradient>
      </defs>
      <polygon class="orange-band" points="0,420 440,420 1100,776 0,776" fill="var(--orange)"/>
      <polygon class="money-stacks" role="img"
        aria-label="Illustration: rising stacks of banknotes with an orange growth arrow ending in a house key"
        points="440,420 640,300 900,180 1100,90 1100,776" fill="url(#moneyTone)"/>
    </svg>

    <div class="brand-mark">
      <span class="brand-mark__dot"></span>
      <span class="brand-mark__name">HARBOURLINE</span>
    </div>

    <h1 class="headline">
      <div class="headline__boost">BOOST</div>
      <div class="headline__sub">YOUR BOOKINGS</div>
    </h1>

    <section class="offer">
      <div class="offer__with">WITH</div>
      <div class="offer__brand">
        <span class="offer__brand-dot"></span>
        <span class="offer__brand-text">
          <span class="offer__brand-name">HARBOURLINE</span>
          <span class="offer__brand-sub">PROPERTY MANAGEMENT</span>
        </span>
      </div>
      <div class="offer__phone">+357 99 482 710</div>
    </section>

    <div class="web-bar">
      <svg class="web-bar__icon" viewBox="0 0 30 30" aria-hidden="true">
        <circle cx="15" cy="15" r="15" fill="var(--orange)"/>
        <polyline points="12,8 19,15 12,22" fill="none" stroke="var(--white)" stroke-width="4" stroke-linecap="round" stroke-linejoin="round"/>
      </svg>
      <span class="web-bar__url">harbourlinehomes.com</span>
    </div>
  </main>
</body>
</html>
```